Football (soccer) board game app design

Hi,

We are a start up looking for a gameplay design for an app. It is a football trivia app that consists of four main screens; login/register, main navigation, gameplay, question.

OVERALL:
We want our app to be kept in a dark theme. Black or very dark gray is preferable, with a couple of nice colors to give it a stylish touch. We like flat designs, but are open for ideas within the general structure design. The logo can be used in the app, but feel free to improve it you feel you can. In the attached material we have tried to outline some of our ideas and other designs friends have helped us make.

LOGIN/REGISTER:
We want a simple login. Email, password, Chatterly login and the possibility to register a new user. Live search check whether the email is valid and free, and there is also live validation of passwords. If this could be incorporated in the design it would be nice.

MAIN NAVIGATION:
In the main navigation screen we want it to be divided into tabs. A home, my games, my categories and a ranking tab. In the top bar it should be possible to search for categories as well as there should be a button to go to settings.

The Home tab
In the home tab we want a "Quick Play" button, and a list of featured categories. A category can be unlocked or locked, which should be illustrated somehow. When a category is tapped it should divide the block into a left and right tap area, where the user can choose to "Beat to unlock" or "Buy to unlock" if locked and "Practice" or "Challenge Friend" if already unlocked.

The My Games tab
In the my games tab, the current games should be divided into three lists. First "your turn", then "opponents turn" and finally "finished games".

The My Categories tab
This tab should include a list of categories, which the user have bought, but as of design it is fairly similar to the blocks in home tab. So not much different here.

The Ranking tab
Ranking should show a set of leaderboards; Today, This Week, This Month, etc. The row in a leaderboard should have teamname and a win percentage.

GAMEPLAY:
The gameplay is inspired by an old football (soccer) board game from the 1950's, and our gameplay consists of three core elements; a football (soccer) pitch, 11 players and a scoreboard.

The football (soccer) pitch
What we need is a pitch seen from behind the goal line. The important issue here, is the perspective, as we want 11 players on the field formed as a 4-3-3 formation, being 1 goalkeeper, 4 defenders, 3 midfielder and 3 strikers. They should all be touchable without overlap. In the other end we want a goal that should be touchable as well. The goal in the nearest end do not have to be visible. Due to the perspective of the field and the fact that players and goal should be touchable, of course give you the opportunity to play around with the proportions of both players and goal. We rather want a large goal being out of proportions, than a small goal with a tiny tap area. Around the field (sidelines and beside the goal) we would like advertising banners like seen on a real stadium.

The players
As mentioned we want 11 players in a 4-3-3 formation. The players should be attached to the board with springs as seen on some of the very old board games, where you could flick the player to pass the ball. This also means that we want the players to be placed in an indentation for the ball to fall into and it would be very cool if you could illustrate the player with the ball, as being pulled back to one of the sides, just enough to see the ball at his feet. The players should be large enough for a user to tap them, hence it would also be beneficial if they are not overlapping. For a start we would like to see the players in a blue shirt and white shorts (socks are not necessary as they are placed on a spring).

Scoreboard
On the scoreboard above the field, we need information such as the names of the two teams (could be FC Brightmoor and Tall Oak Rovers), the score (2-1), minutes played (42), and which half (1st). We also want a progress bar that illustrates how many moves you have used ranging from 0-5. The scoreboard could be inspired from the ones seen around stadiums across the world, but feel free to improvise.

What We Are Looking for
We are looking for full PSD and AI files so we can use them to make minor changes like colors on shirts and shorts, colors on pitch, etc. We really want you to be innovative and inspire us, as we are not designers ourselves. In the attached files, we have tried to sketch out a design that covers our initial ideas. We are looking for a professional look, and having the players and field look like a real board game would just be awesome. A combination of the look from the realistic pitch with advertising banners around it, the idea of our spring-players and the initial thoughts of a design illustrated in our sketch, should help you along. Flat design, cartoonish or somewhere in between is up to you, we just want you to impress and make "wow"-feeling.

QUESTION:
The final screen should display a question with four possible answers. There should be a green/checkmark when correct answer, and a red/cross if incorrect.

That's all. We are looking very much forward to see your designs!
Updates

Hi all,

We have changed the terms of the contest to now have a guaranteed payment, and we are really looking forward to see your designs! Good luck.

/ Mikkel and Anders

By request we have now uploaded an AI-file with the logo for you to play around with. We are looking forward to see your designs.

/ Mikkel and Anders

Reason: Hi designers, We are really happy with the progress being made, and are looking forward to see some of the designs that are still work in progress. However the amount of designs received, has not reached our expectations yet. Therefore we are extending the deadline for seven more days, so designers, that are still working on their designs can continue their work without a stressing deadline in the horizon. Good luck to all of you. We are looking very much forward to see, what you are able to produce. Best regards, Mikkel and Anders

Reason: Hi all, We still have a lot of designers in the competition , who are battling to finish their designs, therefore we have decided to extend the deadline once more. Good luck to all of you!

Target Market(s)

Football (soccer) fans

Industry/Entity Type

Advertising

```html
<!DOCTYPE html>
<html lang="en">
<head>
<meta charset="utf-8">
<title>Goal Mind – App Screens</title>
<link href="https://fonts.googleapis.com/css2?family=Roboto:wght@400;500;700;900&display=swap" rel="stylesheet">
<style>
  :root {
    --backdrop: #4f88a4;
    --backdrop-dark: #3f7591;
    --screen-edge: #0e0e0e;
    --screen-mid: #2e2e2e;
    --header-top: #16488c;
    --header-bottom: #0a2a5c;
    --header-text: #4aa6ea;
    --field-top: #4a4a4a;
    --field-bottom: #2a2a2a;
    --field-line: #8a8a8a;
    --text-light: #f0f0f0;
    --text-muted: #d8d8d8;
    --accent: #2c9be6;
    --accent-dark: #1778c4;
    --social: #2c4f9a;
    --social-dark: #1d3a78;
    --brand: #2b6fc2;
    --brand-large: #1b4f9c;
    --nav-bg: #0d2a55;
    --nav-active: #3a4a5e;
  }
  * { box-sizing: border-box; margin: 0; padding: 0; }
  html, body { width: 1200px; height: 633px; overflow: hidden; }
  body {
    position: relative;
    font-family: "Roboto", Arial, sans-serif;
    background: radial-gradient(ellipse at 40% 40%, var(--backdrop) 0%, var(--backdrop-dark) 100%);
  }
  .screen {
    position: absolute;
    top: 37px;
    width: 229px;
    height: 406px;
    background: radial-gradient(ellipse at 50% 45%, var(--screen-mid) 0%, #1c1c1c 55%, var(--screen-edge) 100%);
    box-shadow: 0 2px 6px rgba(0,0,0,.45);
    overflow: hidden;
  }
  .screen--welcome { left: 9px; }
  .screen--login { left: 249px; }
  .screen--register { left: 487px; }
  .screen--signup { left: 727px; }
  .screen--home { left: 965px; background: #111; }

  .sign-in-bar {
    position: absolute; left: 0; top: 0; width: 100%; height: 21px;
    background: linear-gradient(var(--header-top), var(--header-bottom));
    border-bottom: 1px solid #5d8cc6;
    color: var(--header-text); font-size: 12px; font-weight: 500;
    text-align: center; line-height: 21px;
  }
  .brand-mark {
    position: absolute; left: 0; top: 56px; width: 100%;
    text-align: center; color: var(--brand);
    font-size: 21px; font-weight: 900; letter-spacing: 1px;
  }
  .welcome-label {
    position: absolute; left: 55px; top: 147px;
    color: var(--text-light); font-size: 8px;
  }
  .field {
    position: absolute; left: 55px; width: 127px; height: 23px;
    background: linear-gradient(var(--field-top), var(--field-bottom));
    border: 1px solid var(--field-line); border-radius: 3px;
    color: var(--text-muted); font-size: 7.5px;
    display: flex; align-items: center; gap: 4px; padding-left: 6px;
  }
  .field svg { width: 7px; height: 7px; fill: #ddd; }
  .field--centered { justify-content: center; padding-left: 0; font-weight: 500; }
  .check-badge { position: absolute; left: 167px; top: 173px; width: 29px; height: 29px; }
  .prompt {
    position: absolute; left: 55px; top: 224px;
    color: var(--text-light); font-size: 7.5px;
  }
  .social-button {
    position: absolute; left: 57px; top: 347px; width: 123px; height: 22px;
    background: linear-gradient(var(--social), var(--social-dark));
    border: 1px solid #5a7cc0; border-radius: 3px;
    color: #fff; font-size: 9px; font-weight: 500;
    display: flex; align-items: center; gap: 10px; padding-left: 7px;
  }
  .social-button .square { width: 13px; height: 13px; background: #fff; border-radius: 2px; }

  .tab-bar {
    position: absolute; left: 0; top: 0; width: 100%; height: 33px;
    background: linear-gradient(#15407a, var(--nav-bg));
    display: flex; padding-left: 20px;
  }
  .tab {
    width: 47px; height: 33px; color: #fff; font-size: 6px;
    display: flex; flex-direction: column; align-items: center; justify-content: center; gap: 3px;
  }
  .tab--active { background: linear-gradient(#5a6878, var(--nav-active)); }
  .tab svg { width: 17px; height: 17px; }
  .action-button {
    position: absolute; top: 37px; height: 19px; width: 101px;
    background: linear-gradient(#4bb3f3, var(--accent-dark));
    border: 1px solid #9ad4fa; border-radius: 2px;
    color: #fff; font-size: 7.5px; font-weight: 500;
    display: flex; align-items: center; justify-content: center; gap: 5px;
  }
  .action-button--quick { left: 9px; }
  .action-button--challenge { left: 117px; }
  .action-button svg { width: 8px; height: 8px; }
  .section-title {
    position: absolute; left: 0; top: 62px; width: 100%;
    text-align: center; color: #fff; font-size: 7.5px;
  }
  .category {
    position: absolute; left: 0; width: 100%; height: 63px;
    border-top: 1px solid #0a0a0a;
  }
  .category__photo { position: absolute; inset: 0; }
  .category__title {
    position: absolute; left: 6px; top: 10px;
    color: #fff; font-size: 9px; font-weight: 500; text-shadow: 0 1px 2px #000;
  }
  .category__brand {
    position: absolute; left: 8px; bottom: 8px;
    color: var(--brand); font-size: 8px; font-weight: 900;
  }
  .category__lock { position: absolute; right: 18px; top: 6px; width: 9px; height: 9px; }
  .category__chevron { position: absolute; right: 3px; top: 22px; width: 8px; height: 18px; }
  .photo--league { background: linear-gradient(110deg, #2a4a8a, #6f86b4 50%, #c8d0e0); }
  .photo--keeper { background: linear-gradient(110deg, #2b2b2b, #6d6d6d 55%, #a9a9a9); }
  .photo--cup { background: linear-gradient(110deg, #1f3450, #4c6a3a 55%, #8a8a3a); }
  .photo--harbor { background: linear-gradient(110deg, #3a2a3a, #8a2a2a 55%, #b8484a); }
  .photo--arena { background: linear-gradient(110deg, #1e2a4a, #35507a 55%, #6a6a44); }

  .showcase-brand {
    position: absolute; left: 908px; top: 478px; width: 273px;
    text-align: center; color: var(--brand-large);
    font-size: 52px; font-weight: 900; line-height: 1.05; letter-spacing: 2px;
  }
</style>
</head>
<body>

<svg width="0" height="0" style="position:absolute">
  <defs>
    <symbol id="icon-user" viewBox="0 0 10 10"><circle cx="5" cy="3" r="2.3"/><path d="M0.5 10c0-3 2-4.5 4.5-4.5S9.5 7 9.5 10z"/></symbol>
    <symbol id="icon-lock" viewBox="0 0 10 10"><path d="M2.5 4.5V3a2.5 2.5 0 0 1 5 0v1.5" fill="none" stroke="currentColor" stroke-width="1.3"/><rect x="1.5" y="4.5" width="7" height="5.5" rx="0.8"/></symbol>
    <symbol id="icon-check" viewBox="0 0 30 30"><circle cx="15" cy="15" r="14" fill="#e8eef4"/><circle cx="15" cy="15" r="12" fill="#2c9be6"/><path d="M8.5 15.5l4.5 4.5 8.5-9.5" fill="none" stroke="#fff" stroke-width="3" stroke-linecap="round" stroke-linejoin="round"/></symbol>
  </defs>
</svg>

<section class="screen screen--welcome">
  <div class="brand-mark">GOAL MIND</div>
  <div class="field" style="top:165px"><svg><use href="#icon-user"/></svg>Email</div>
  <div class="social-button"><span class="square"></span>Login with Chatterly</div>
</section>

<section class="screen screen--login">
  <div class="sign-in-bar">Sign In</div>
  <div class="brand-mark">GOAL MIND</div>
  <div class="welcome-label">Welcome Back</div>
  <div class="field" style="top:163px"><svg><use href="#icon-user"/></svg>Email</div>
  <div class="field" style="top:189px"><svg><use href="#icon-lock"/></svg>Password</div>
  <svg class="check-badge"><use href="#icon-check"/></svg>
  <div class="social-button"><span class="square"></span>Login with Chatterly</div>
</section>

<section class="screen screen--register">
  <div class="sign-in-bar">Sign In</div>
  <div class="brand-mark">GOAL MIND</div>
  <div class="welcome-label">Welcome Back</div>
  <div class="field" style="top:163px"><svg><use href="#icon-user"/></svg>Email</div>
  <div class="field" style="top:189px"><svg><use href="#icon-lock"/></svg>Password</div>
  <div class="field" style="top:215px">Confirm Password</div>
  <svg class="check-badge"><use href="#icon-check"/></svg>
  <div class="social-button"><span class="square"></span>Login with Chatterly</div>
</section>

<section class="screen screen--signup">
  <div class="sign-in-bar">Sign In</div>
  <div class="brand-mark">GOAL MIND</div>
  <div class="welcome-label">Welcome Back</div>
  <div class="field" style="top:163px"><svg><use href="#icon-user"/></svg>Email</div>
  <div class="field" style="top:189px"><svg><use href="#icon-lock"/></svg>Password</div>
  <svg class="check-badge"><use href="#icon-check"/></svg>
  <div class="prompt" style="top:224px">Don't have an account yet?</div>
  <div class="field field--centered" style="top:236px">SIGN UP</div>
  <div class="social-button"><span class="square"></span>Login with Chatterly</div>
</section>

<section class="screen screen--home">
  <nav class="tab-bar">
    <div class="tab tab--active">
      <svg viewBox="0 0 20 20"><circle cx="10" cy="10" r="8.5" fill="none" stroke="#fff" stroke-width="1.5"/><path d="M6 7.5h8M6 10h8M6 12.5h8" stroke="#fff" stroke-width="1.4"/></svg>HOME</div>
    <div class="tab">
      <svg viewBox="0 0 20 20"><circle cx="10" cy="10" r="8.5" fill="none" stroke="#fff" stroke-width="1.5"/><circle cx="10" cy="10" r="3" fill="none" stroke="#fff" stroke-width="1.2"/></svg>MATCHS</div>
    <div class="tab">
      <svg viewBox="0 0 20 20"><circle cx="10" cy="10" r="8.5" fill="none" stroke="#fff" stroke-width="1.5"/><path d="M10 5l1.5 3.2 3.4.4-2.5 2.3.7 3.4-3.1-1.7-3.1 1.7.7-3.4-2.5-2.3 3.4-.4z" fill="none" stroke="#fff" stroke-width="1"/></svg>RANKING</div>
    <div class="tab">
      <svg viewBox="0 0 20 20"><circle cx="10" cy="10" r="6" fill="none" stroke="#fff" stroke-width="3" stroke-dasharray="2.4 2.3"/><circle cx="10" cy="10" r="3" fill="none" stroke="#fff" stroke-width="1.2"/></svg>SETTINGS</div>
  </nav>

  <div class="action-button action-button--quick">
    <svg viewBox="0 0 10 10"><circle cx="5" cy="5" r="4.5" fill="#fff"/><circle cx="5" cy="5" r="1.6" fill="#222"/></svg>Quick Play</div>
  <div class="action-button action-button--challenge">
    <svg style="fill:#fff"><use href="#icon-user"/></svg>Challenge Friend</div>

  <div class="section-title">Choose Game Category</div>

  <article class="category" style="top:80px">
    <div class="category__photo photo--league" role="img" aria-label="Photo of players contesting a header in a league match"></div>
    <div class="category__title">Nordic League</div>
    <div class="category__brand">GOAL MIND</div>
    <svg class="category__lock" style="fill:#fff;color:#fff"><use href="#icon-lock"/></svg>
    <svg class="category__chevron" viewBox="0 0 8 18"><path d="M1 1l6 8-6 8" fill="none" stroke="#fff" stroke-width="1.5"/></svg>
  </article>
  <article class="category" style="top:143px">
    <div class="category__photo photo--keeper" role="img" aria-label="Photo of a goalkeeper diving for a save"></div>
    <div class="category__title">Legendary Goalkeeper</div>
    <div class="category__brand">GOAL MIND</div>
    <svg class="category__lock" style="fill:#fff;color:#fff"><use href="#icon-lock"/></svg>
    <svg class="category__chevron" viewBox="0 0 8 18"><path d="M1 1l6 8-6 8" fill="none" stroke="#fff" stroke-width="1.5"/></svg>
  </article>
  <article class="category" style="top:206px">
    <div class="category__photo photo--cup" role="img" aria-label="Photo of a tournament match on a floodlit pitch"></div>
    <div class="category__title">Summer Cup 1994</div>
    <div class="category__brand">GOAL MIND</div>
    <svg class="category__lock" style="fill:#fff;color:#fff"><use href="#icon-lock"/></svg>
    <svg class="category__chevron" viewBox="0 0 8 18"><path d="M1 1l6 8-6 8" fill="none" stroke="#fff" stroke-width="1.5"/></svg>
  </article>
  <article class="category" style="top:269px">
    <div class="category__photo photo--harbor" role="img" aria-label="Photo of a striker running with the ball"></div>
    <div class="category__title">Rivera Harbor</div>
    <div class="category__brand">GOAL MIND</div>
    <svg class="category__lock" style="fill:#fff;color:#fff"><use href="#icon-lock"/></svg>
    <svg class="category__chevron" viewBox="0 0 8 18"><path d="M1 1l6 8-6 8" fill="none" stroke="#fff" stroke-width="1.5"/></svg>
  </article>
  <article class="category" style="top:332px;height:74px">
    <div class="category__photo photo--arena" role="img" aria-label="Photo of a match in a packed stadium"></div>
    <div class="category__title" style="top:7px">RIVERSIDE ARENA</div>
    <div class="category__brand">GOAL MIND</div>
    <svg class="category__lock" style="fill:#fff;color:#fff"><use href="#icon-lock"/></svg>
    <svg class="category__chevron" viewBox="0 0 8 18" style="top:32px"><path d="M1 1l6 8-6 8" fill="none" stroke="#fff" stroke-width="1.5"/></svg>
  </article>
</section>

<div class="showcase-brand">GOAL<br>MIND</div>

</body>
</html>
```